Fitness Training academy needs a business card design

We need a business card design for a NEW business that teaches/trains people how to become personal trainers. We would like to see designs both with and without our QR code. We would like our designs double sided.

See the following attachments
Design Brief
Logos (both black background, white background in all formats)
QR Code

Industry/Entity Type

Business

```html
<!DOCTYPE html>
<html lang="en">
<head>
<meta charset="utf-8">
<title>Summit Trainer Academy – Business Card</title>
<link href="https://fonts.googleapis.com/css2?family=Michroma&display=swap" rel="stylesheet">
<style>
  :root {
    --bg: #d9d9d9;
    --card-white: #ffffff;
    --card-black: #0b0b0b;
    --ink: #2b2b2b;
    --ink-soft: #5a5a5a;
    --brand-grey: #7a7a7a;
    --brand-red: #e3241b;
    --brand-orange: #f26a21;
    --divider: #bdbdbd;
  }
  * { box-sizing: border-box; margin: 0; padding: 0; }
  html, body { width: 1200px; height: 770px; overflow: hidden; }
  body {
    background: var(--bg);
    font-family: "Michroma", sans-serif;
    display: flex;
    align-items: center;
    justify-content: space-between;
    padding: 0 27px;
  }
  .card {
    position: relative;
    width: 560px;
    height: 320px;
    overflow: hidden;
    box-shadow: 0 6px 18px rgba(0,0,0,.18);
  }

  /* Front */
  .card--front { background: var(--card-white); }
  .brand {
    position: absolute;
    display: flex;
    align-items: center;
    gap: 14px;
  }
  .card--front .brand { left: 150px; top: 38px; }
  .brand__dot {
    width: 40px; height: 40px; border-radius: 50%;
    background: var(--brand-orange);
    flex: none;
  }
  .brand__name {
    font-size: 16px;
    color: var(--brand-grey);
    letter-spacing: .5px;
    white-space: nowrap;
  }
  .identity {
    position: absolute;
    right: 305px;
    top: 122px;
    text-align: right;
    color: var(--ink-soft);
    font-size: 10px;
    line-height: 1.7;
  }
  .identity__name { font-size: 13px; color: var(--ink); letter-spacing: 1px; }
  .identity__role { margin-bottom: 8px; }
  .divider {
    position: absolute;
    left: 272px; top: 124px;
    width: 1px; height: 100px;
    background: var(--divider);
  }
  .contacts {
    position: absolute;
    left: 290px; top: 124px;
    list-style: none;
    font-size: 10.5px;
    color: var(--ink);
    line-height: 1;
  }
  .contacts li { display: flex; align-items: center; gap: 8px; margin-bottom: 9px; }
  .contacts svg { width: 13px; height: 13px; flex: none; }
  .band { position: absolute; left: 0; bottom: 0; width: 560px; height: 80px; }
  .band__url {
    position: absolute;
    left: 178px; bottom: 28px;
    font-size: 10px;
    color: #fff;
    letter-spacing: .5px;
  }

  /* Back */
  .card--back { background: var(--card-black); }
  .card--back .brand { left: 96px; top: 130px; gap: 20px; }
  .card--back .brand__dot { width: 60px; height: 60px; }
  .card--back .brand__name { color: #a9a9a9; font-size: 16px; }
</style>
</head>
<body>

<section class="card card--front" aria-label="Card front">
  <div class="brand">
    <span class="brand__dot"></span>
    <span class="brand__name">SUMMIT TRAINER ACADEMY</span>
  </div>

  <div class="identity">
    <p class="identity__name">MARCUS HALE</p>
    <p class="identity__role">Owner / C.E.O</p>
    <p>Suite # 410, Oak Bldg,</p>
    <p>NY 10452</p>
  </div>

  <span class="divider"></span>

  <ul class="contacts">
    <li>
      <svg viewBox="0 0 16 16"><circle cx="8" cy="8" r="8" fill="var(--brand-orange)"/><path d="M5 4.5l1.6-.4 1 2-1 .8a5 5 0 0 0 2.5 2.5l.8-1 2 1-.4 1.6C8 11.5 4.5 8 5 4.5z" fill="#fff"/></svg>
      <span>555-201-4480</span>
    </li>
    <li>
      <svg viewBox="0 0 16 16"><circle cx="8" cy="8" r="8" fill="var(--brand-orange)"/><rect x="5.5" y="3.5" width="5" height="9" rx="1" fill="#fff"/></svg>
      <span>555-201-4481</span>
    </li>
    <li>
      <svg viewBox="0 0 16 16"><circle cx="8" cy="8" r="8" fill="var(--brand-orange)"/><rect x="4" y="6" width="8" height="5" fill="#fff"/><rect x="5.5" y="3.5" width="5" height="2.5" fill="#fff"/></svg>
      <span>555-201-4482</span>
    </li>
    <li>
      <svg viewBox="0 0 16 16"><circle cx="8" cy="8" r="8" fill="var(--brand-orange)"/><rect x="4" y="5" width="8" height="6" fill="#fff"/><path d="M4 5l4 3 4-3" stroke="var(--brand-orange)" fill="none"/></svg>
      <span>marcus@summittrainer.com</span>
    </li>
    <li>
      <svg viewBox="0 0 16 16"><circle cx="8" cy="8" r="8" fill="var(--brand-orange)"/><circle cx="8" cy="8" r="4" fill="none" stroke="#fff" stroke-width="1.2"/><path d="M4 8h8M8 4v8" stroke="#fff" stroke-width="1"/></svg>
      <span>www.summittrainer.com</span>
    </li>
  </ul>

  <svg class="band" viewBox="0 0 560 80" aria-hidden="true">
    <defs>
      <linearGradient id="tabFill" x1="0" x2="1">
        <stop offset="0" stop-color="var(--brand-red)"/>
        <stop offset=".55" stop-color="var(--brand-orange)"/>
        <stop offset="1" stop-color="var(--brand-red)"/>
      </linearGradient>
    </defs>
    <rect x="0" y="30" width="150" height="2" fill="var(--brand-red)"/>
    <rect x="0" y="38" width="150" height="4" fill="var(--brand-red)"/>
    <rect x="150" y="20" width="250" height="44" rx="12" fill="url(#tabFill)"/>
    <rect x="400" y="48" width="160" height="2" fill="var(--brand-red)"/>
    <rect x="400" y="56" width="160" height="4" fill="var(--brand-red)"/>
    <rect x="0" y="68" width="560" height="12" fill="var(--brand-red)"/>
  </svg>
  <span class="band__url">www.summittrainer.com</span>
</section>

<section class="card card--back" aria-label="Card back">
  <div class="brand">
    <span class="brand__dot"></span>
    <span class="brand__name">SUMMIT TRAINER ACADEMY</span>
  </div>
</section>

</body>
</html>
```